Geschäftspapiere für Handwerksunternehmen
Zielgruppe
Handwerk
Elektroinstallation
Design Modern
Aufgabenstellung
Anschrift, Kontaktdaten, Bankverbindung, Logo,
Im Lindengrund 7 47391 Tannbergen Inhaber Jonas Velbrück
Telefon: 04128-6350712 Email: info@trolvane-elektrotechnik.de Internet: www.trolvane-elektrotechnik.de
Finanzamt Hobrachtal USt.-ID: DE574036218 Steuer Nr.:3196450721
Kreiskasse Wendorn IBAN:DE71430982160004197356 BIC:WKRNDEF1WDN

```html
<!DOCTYPE html>
<html lang="de">
<head>
<meta charset="utf-8">
<title>Trolvane Elektrotechnik – Briefumschlag</title>
<link rel="stylesheet" href="https://fonts.googleapis.com/css2?family=Arimo:wght@400;700&display=swap">
<style>
  :root {
    --stage: #e6e6e6;
    --paper: #ffffff;
    --charcoal: #3a3a3a;
    --accent: #f2e52a;
    --slate: #6e7a89;
    --window: #d7ebf8;
    --ink: #555a60;
    --shadow: rgba(0,0,0,0.28);
  }
  html, body {
    margin: 0;
    padding: 0;
    width: 1200px;
    height: 1200px;
    overflow: hidden;
    background: var(--stage);
    font-family: "Arimo", Arial, sans-serif;
  }
  .canvas { position: relative; width: 1200px; height: 1200px; }

  .envelope {
    position: absolute;
    left: 72px;
    width: 1032px;
    height: 516px;
    background: var(--paper);
    box-shadow: 8px 8px 10px var(--shadow);
    overflow: hidden;
  }
  .envelope--back { top: 40px; }
  .envelope--front { top: 619px; }

  .flap { position: absolute; left: 0; top: 0; width: 1032px; height: 146px; }

  .flap-name {
    position: absolute;
    top: 56px;
    left: 0;
    width: 1032px;
    text-align: center;
    font-weight: 700;
    font-size: 26px;
    color: var(--accent);
    letter-spacing: 0.5px;
  }

  .brand {
    position: absolute;
    left: 84px;
    top: 62px;
    display: flex;
    align-items: center;
    gap: 14px;
  }
  .brand-dot {
    width: 34px;
    height: 34px;
    border-radius: 50%;
    background: var(--accent);
  }
  .brand-name {
    font-weight: 700;
    font-size: 34px;
    color: var(--charcoal);
    letter-spacing: 0.3px;
  }

  .sender {
    position: absolute;
    left: 95px;
    top: 161px;
    display: flex;
    align-items: center;
    gap: 19px;
  }
  .sender-pin { width: 46px; height: 46px; }
  .sender-address { font-size: 17px; color: var(--ink); }

  .address-window {
    position: absolute;
    left: 82px;
    top: 259px;
    width: 387px;
    height: 185px;
    border-radius: 26px;
    background: var(--window);
  }

  .services { position: absolute; left: 0; top: 0; width: 1032px; height: 516px; pointer-events: none; }
  .service-label {
    font-family: "Arimo", Arial, sans-serif;
    font-size: 7px;
    font-weight: 700;
    fill: var(--accent);
  }
  .web-label {
    font-family: "Arimo", Arial, sans-serif;
    font-size: 10px;
    fill: var(--slate);
  }
</style>
</head>
<body>
<main class="canvas">

  <section class="envelope envelope--back" aria-label="Umschlag Rückseite">
    <svg class="flap" viewBox="0 0 1032 146" aria-hidden="true">
      <path d="M0 0 H1032 L994 122 Q986 144 962 144 H70 Q46 144 40 122 Z" fill="var(--charcoal)"/>
    </svg>
    <div class="flap-name">Trolvane Elektrotechnik</div>
  </section>

  <section class="envelope envelope--front" aria-label="Umschlag Vorderseite">
    <div class="brand">
      <span class="brand-dot"></span>
      <span class="brand-name">Trolvane Elektrotechnik</span>
    </div>

    <div class="sender">
      <svg class="sender-pin" viewBox="0 0 46 46" aria-hidden="true">
        <circle cx="23" cy="23" r="22" fill="var(--accent)"/>
        <circle cx="23" cy="23" r="19" fill="var(--charcoal)"/>
        <path d="M33 13 L15 21 L23 23 L25 31 Z" fill="var(--accent)"/>
      </svg>
      <span class="sender-address">Im Lindengrund 7 47391 Tannbergen</span>
    </div>

    <div class="address-window" aria-label="Adressfenster"></div>

    <svg class="services" viewBox="0 0 1032 516" aria-label="Leistungen">
      <g fill="none" stroke="var(--slate)" stroke-width="1.6">
        <circle cx="490" cy="465" r="7"/>
        <path d="M486 472 v6 h8 v-6"/>
        <path d="M478 455 l4 3 M502 455 l-4 3 M490 450 v4 M475 465 h3 M505 465 h-3"/>
      </g>
      <path d="M577 452 l-8 16 h6 l-4 14 l10 -18 h-6 l5 -12 Z" fill="var(--slate)"/>
      <path d="M648 464 L666 449 L684 464 H679 V480 H653 V464 Z" fill="var(--slate)"/>
      <rect x="662" y="468" width="8" height="8" fill="var(--paper)"/>
      <g fill="var(--slate)">
        <path d="M738 462 H768 L772 478 H734 Z"/>
        <rect x="752" y="478" width="3" height="6"/>
      </g>
      <g stroke="var(--paper)" stroke-width="1">
        <line x1="737" y1="470" x2="770" y2="470"/>
        <line x1="748" y1="462" x2="746" y2="478"/>
        <line x1="758" y1="462" x2="760" y2="478"/>
      </g>
      <circle cx="768" cy="456" r="4" fill="var(--slate)"/>

      <path d="M0 490 H803 L796 502 H0 Z" fill="var(--slate)"/>
      <path d="M808 490 H1032 V516 H0 V504 H800 Z" fill="var(--accent)"/>

      <g stroke="var(--paper)" stroke-width="1.4">
        <line x1="534" y1="490" x2="528" y2="502"/>
        <line x1="628" y1="490" x2="622" y2="502"/>
        <line x1="716" y1="490" x2="710" y2="502"/>
      </g>

      <text class="service-label" x="490" y="499" text-anchor="middle">Beleuchtung</text>
      <text class="service-label" x="576" y="499" text-anchor="middle">Elektroinstallation</text>
      <text class="service-label" x="666" y="499" text-anchor="middle">Smart Home</text>
      <text class="service-label" x="752" y="499" text-anchor="middle">Photovoltaik</text>

      <g fill="none" stroke="var(--slate)" stroke-width="1">
        <circle cx="855" cy="502" r="5.5"/>
        <ellipse cx="855" cy="502" rx="2.4" ry="5.5"/>
        <line x1="849.5" y1="502" x2="860.5" y2="502"/>
      </g>
      <text class="web-label" x="867" y="505.5">www.trolvane-elektrotechnik.de</text>
    </svg>
  </section>

</main>
</body>
</html>
```